Amber Kite Foundation Inforgraphic

We are in need of an infographic layout to highlight facts for a medical foundation - the Amber Kite Foundation. We are a foundation dedicated to early detection and screening of pulmonary arterial hypertension, a deadly combination heart and lung disease We need a graphic that incorporates the following facts:

(1) Pulmonary Hypertension Symptoms: •Chest Pain
•Dizziness
•Shortness of Breath
•Fatigue
•Edema or swelling
•Cyanosis or skin discoloration

(2) Typically PH patients are consulted by 3 or more physicians before diagnosis

(3) PH patient’s generally incur 2.8 years between symptom onset and diagnosis via right heart catheterization

(4) Left untreated, the average life expectancy of a PAH patient is approximately 3 years from symptom onset

(5) No improvement has been achieved in early detection rates of PH since 1995

(6) 5 year survival rates are measured at 86% for PH patients diagnosed in early stages. 5 year survival rates for PH patients diagnosed late stages decrease to 50%

We want to incorporate these highlights into a fun and easy to follow infographic that can be transferred onto a large scale display banner.

We want to utilize our logo somewhere on the graphic. The logo file is attached. We also want to incorporate our slogan: Igniting the (ph)ight against pulmonary arterial hypertension through early detection and screening.

Thanks.

Industry/Entity Type

Medical

Colors
0555a3
3176b5
85acd3

Requirements
Must have
• Amber Kite Foundation Logo
• Dynamic display of graphics and figures to highlight statistics in the project discription

```html
<!DOCTYPE html>
<html lang="en">
<head>
<meta charset="utf-8">
<title>Chest Pain – Pulmonary Hypertension Facts | Amber Kite Foundation</title>
<link href="https://fonts.googleapis.com/css2?family=Oswald:wght@500;600&family=Libre+Franklin:wght@600;700&display=swap" rel="stylesheet">
<style>
  :root {
    --blue-deep: #0555a3;
    --blue-mid: #3176b5;
    --blue-soft: #85acd3;
    --blue-bar: #8aafd6;
    --ink: #14253f;
    --white: #ffffff;
    --page: #ffffff;
  }
  * { margin: 0; padding: 0; box-sizing: border-box; }
  html, body { width: 1200px; height: 2290px; overflow: hidden; background: var(--page); }
  .infographic { position: relative; width: 1200px; height: 2290px; overflow: hidden; font-family: "Libre Franklin", Arial, sans-serif; color: var(--ink); }

  .header-band {
    position: absolute; left: 0; top: 0; width: 1200px; height: 222px;
    background: linear-gradient(135deg, #1f5ea8 0%, var(--blue-deep) 55%, #1a4f95 100%);
  }
  .header-band::after {
    content: ""; position: absolute; left: 0; right: 0; bottom: 0; height: 6px;
    background: var(--blue-soft);
  }
  .title {
    position: absolute; left: 0; width: 1200px; top: 14px; text-align: center;
    font-family: "Oswald", "Arial Narrow", sans-serif; font-weight: 600;
    font-size: 90px; letter-spacing: 1px; color: var(--white);
  }
  .ribbon-tab { position: absolute; background: var(--blue-deep); }
  .ribbon {
    position: absolute; background: var(--blue-mid); color: var(--white);
    font-family: "Oswald", "Arial Narrow", sans-serif; font-weight: 500;
    display: flex; align-items: center; justify-content: center; letter-spacing: 1px;
  }
  .symptoms-ribbon { left: 157px; top: 168px; width: 886px; height: 99px; font-size: 42px; }
  .tab-left { left: 81px; top: 196px; width: 100px; height: 97px; }
  .tab-right { left: 1019px; top: 196px; width: 100px; height: 97px; }

  .symptom {
    position: absolute; width: 222px; height: 222px; border-radius: 50%;
    background: var(--blue-mid); color: var(--white);
    display: flex; align-items: center; justify-content: center; text-align: center;
    font-weight: 700; font-size: 28px; line-height: 1.3;
  }
  .photo-ring {
    position: absolute; left: 445px; top: 545px; width: 300px; height: 300px; border-radius: 50%;
    background: var(--blue-soft); padding: 10px;
  }
  .photo-ring .photo {
    width: 100%; height: 100%; border-radius: 50%;
    background: radial-gradient(circle at 50% 40%, #e9d2c4 0%, #9fb4d4 45%, #4f7fbc 100%);
  }

  .fact-bar {
    position: absolute; background: var(--blue-bar); display: flex; align-items: center;
    font-weight: 700; font-size: 27px; line-height: 1.35; color: var(--ink);
  }
  .fact-badge {
    position: absolute; width: 190px; height: 190px; border-radius: 50%;
    background: var(--blue-mid); color: var(--white); text-align: center;
    display: flex; flex-direction: column; align-items: center; justify-content: center;
  }
  .badge-number { font-size: 74px; font-weight: 700; line-height: 1; }
  .badge-unit { font-size: 38px; font-weight: 700; line-height: 1.1; }
  .badge-year .badge-unit { font-size: 44px; }
  .badge-year .badge-number { font-size: 60px; }
  .physician-icon { display: block; width: 90px; height: 150px; }

  .survival-strip { position: absolute; left: 0; top: 1927px; width: 947px; height: 86px; background: var(--blue-deep); }
  .survival-ribbon { left: 64px; top: 1919px; width: 809px; height: 71px; font-family: "Libre Franklin", Arial, sans-serif; font-weight: 600; font-size: 40px; letter-spacing: 0; }
  .survival-box {
    position: absolute; left: 92px; top: 1990px; width: 759px; height: 300px;
    background: var(--blue-bar); padding: 30px 40px 0 44px;
    font-weight: 700; font-size: 27px; line-height: 1.4;
  }
  .survival-box p + p { margin-top: 38px; }

  .foundation-mark {
    position: absolute; left: 960px; top: 2118px; width: 220px; text-align: center;
    color: var(--blue-deep);
  }
  .mark-dot { width: 60px; height: 60px; border-radius: 50%; background: var(--blue-mid); margin: 0 auto 14px; }
  .mark-name { font-family: "Libre Franklin", Arial, sans-serif; font-weight: 600; font-size: 26px; letter-spacing: 2px; line-height: 1.2; }
</style>
</head>
<body>
<main class="infographic">
  <header class="header-band" role="img" aria-label="Dark blue header band with diagonal stripes"></header>
  <h1 class="title">CHEST PAIN</h1>

  <div class="ribbon-tab tab-left"></div>
  <div class="ribbon-tab tab-right"></div>
  <h2 class="ribbon symptoms-ribbon">PULMONARY HYPERTENSION SYMPTOMS:</h2>

  <section class="symptoms">
    <div class="symptom" style="left:484px; top:309px;">Dizziness</div>
    <div class="symptom" style="left:199px; top:523px;">Fatigue</div>
    <div class="symptom" style="left:787px; top:533px;">Shortness<br>of Breath</div>
    <div class="symptom" style="left:304px; top:848px;">Cyanosis<br>or Skin<br>discoloration</div>
    <div class="symptom" style="left:668px; top:851px;">Edema<br>or<br>Swelling</div>
    <div class="photo-ring">
      <div class="photo" role="img" aria-label="Photo of a doctor listening to a patient's chest with a stethoscope"></div>
    </div>
  </section>

  <section class="facts">
    <div class="fact-bar" style="left:221px; top:1148px; width:935px; height:107px; padding-left:46px;">
      Typically PH patients are consulted by 3 or more Physicians<br>before diagnosis
    </div>
    <div class="fact-badge" style="left:50px; top:1104px;">
      <div class="physician-icon" role="img" aria-label="Illustration of a physician in a white coat" style="background:linear-gradient(#ffffff,#dfe9f5); border-radius:40px 40px 8px 8px;"></div>
    </div>

    <div class="fact-bar" style="left:49px; top:1309px; width:1012px; height:149px; padding-left:34px;">
      PH patient’s generally incur 2.8 years between symptom<br>onset and diagnosis via right heart catheterization
    </div>
    <div class="fact-badge" style="left:971px; top:1299px;">
      <span class="badge-number">2.8</span><span class="badge-unit">Years</span>
    </div>

    <div class="fact-bar" style="left:229px; top:1535px; width:927px; height:111px; padding-left:30px;">
      Left untreated, the average life expectancy of a PAH patient<br>is approximately 3 years from symptom onset
    </div>
    <div class="fact-badge" style="left:50px; top:1493px;">
      <span class="badge-number">3</span><span class="badge-unit">years</span>
    </div>

    <div class="fact-bar" style="left:49px; top:1721px; width:1005px; height:130px; padding-left:34px;">
      No improvement has been achieved in early detection<br>rates of PH since 1995
    </div>
    <div class="fact-badge badge-year" style="left:971px; top:1695px;">
      <span class="badge-unit">Since</span><span class="badge-number">1995</span>
    </div>
  </section>

  <section class="survival">
    <div class="survival-strip"></div>
    <h2 class="ribbon survival-ribbon">5 year survival rates</h2>
    <div class="survival-box">
      <p>5 year survival rates are measured at 86% for<br>PH patients diagnosed in early stages.</p>
      <p>5 year survival rates for PH patients diagnosed<br>late stages decrease to 50%</p>
    </div>
  </section>

  <footer class="foundation-mark">
    <div class="mark-dot"></div>
    <div class="mark-name">AMBER KITE<br>FOUNDATION</div>
  </footer>
</main>
</body>
</html>
```